Flyer "Pinch Analysis"-Energy Optimization procedure for Industry

We need a flyer (1xA4 recto/verso )design for a new part of our business.

In Summary: we want to communicate that we are providing "Pinch Analysis" for the industry. It's an energy optimization procedure. We are a cutting edge engineering consulting group.

All details about project in the attached files

Target Market(s)

Engineering

Industry/Entity Type

Business

Font styles to use
Serif

Requirements
Must have
• Finale document in .ai format ready for printing
• More informations in attached files
Nice to have
• See attached files

```html
<!DOCTYPE html>
<html lang="fr">
<head>
<meta charset="utf-8">
<title>Analyse Pinch – Thermalys</title>
<link href="https://fonts.googleapis.com/css2?family=Exo+2:wght@300;400;700;800&display=swap" rel="stylesheet">
<style>
  :root{
    --navy:#0f2f5c;
    --steel:#1c4a72;
    --white:#ffffff;
    --sky-top:#4db4e4;
    --sky-mid:#3f95c7;
    --steel-low:#6f8ea5;
    --band:rgba(20,45,70,.72);
    --accent:#4fb8ea;
  }
  *{margin:0;padding:0;box-sizing:border-box}
  html,body{width:849px;height:1200px;overflow:hidden;background:#fff}
  body{font-family:"Exo 2",sans-serif;color:var(--white)}
  .flyer{position:relative;width:849px;height:1200px;overflow:hidden}
  .backdrop{position:absolute;inset:0;
    background:
      radial-gradient(circle at 624px 700px, rgba(235,245,250,.85) 0 190px, rgba(160,195,215,.6) 230px, rgba(0,0,0,0) 270px),
      radial-gradient(ellipse at 180px 900px, rgba(200,220,232,.55), rgba(0,0,0,0) 320px),
      linear-gradient(180deg,var(--sky-top) 0%,var(--sky-mid) 35%,#5d8fb0 60%,var(--steel-low) 80%,#8aa3b5 100%);}
  .headline{position:absolute;left:53px;top:56px;width:360px;font-weight:800;font-size:27.5px;line-height:38px;color:var(--white)}
  .headline .lead{color:var(--navy)}
  .headline .indent{padding-left:42px}
  .tagline{position:absolute;left:53px;top:220px;width:360px;font-weight:300;font-size:27px;line-height:34px;color:var(--steel)}
  .tagline .indent{padding-left:47px}
  .tagline .indent-lg{padding-left:38px}
  .body{font-size:13.2px;line-height:18.2px;font-weight:400}
  .body p{margin-bottom:18px}
  .intro{position:absolute;left:55px;top:407px;width:310px}
  .benefits{list-style:none}
  .benefits li{padding-left:12px;text-indent:-12px}
  .benefits li::before{content:"• "}
  .details{position:absolute;left:437px;top:58px;width:365px}
  .details strong{font-weight:700}
  .contact-band{position:absolute;left:0;top:979px;width:849px;height:98px;background:var(--band)}
  .contact{position:absolute;left:68px;top:996px;font-size:17.5px;line-height:21px;letter-spacing:.5px}
  .contact h2{font-size:17.5px;font-weight:800;letter-spacing:1px}
  .brand{position:absolute;left:400px;top:1000px;display:flex;align-items:center;gap:14px}
  .brand-mark{width:26px;height:26px;background:var(--accent)}
  .brand-name{font-weight:800;font-size:40px;color:var(--accent);letter-spacing:1px}
  .brand-sub{margin-left:8px;padding-left:12px;border-left:1px solid var(--white);font-size:14.5px;line-height:17px;font-weight:700;letter-spacing:.8px;color:var(--white)}
  .address{position:absolute;left:71px;top:1090px;font-size:15px;line-height:18.5px;letter-spacing:.8px}
</style>
</head>
<body>
<main class="flyer">
  <div class="backdrop" role="img" aria-label="Photographie d'un manomètre thermique en degrés Celsius monté sur des conduites industrielles en acier, tons bleutés"></div>

  <h1 class="headline">
    <span class="lead">Analyse Pinch</span> - en route<br>
    <span class="indent">vers la performance</span><br>
    opérationnelle et<br>
    l'efficacité énergétique
  </h1>

  <p class="tagline">
    <span class="indent">La performance</span><br>
    opérationnelle et<br>
    <span class="indent-lg">l'efficacité énergétique</span><br>
    sont les clés de la réussite<br>
    de l'industrie de demain.
  </p>

  <section class="intro body">
    <p>Fort d'une longue expérience dans l'analyse, la conception et la mise en service d'installations industrielles (chimie, alimentaire, pharmacie,…), la société Thermalys utilise l'analyse Pinch dans sa démarche de conception et d'amélioration.</p>
    <p>L'analyse Pinch est une méthode d'analyse systématique développée et appliquée depuis les années 1980; elle permet de répondre aux questions suivantes:</p>
    <ul class="benefits">
      <li>Quels sont les besoins de chaleur et de froid minimaux de mon procédé</li>
      <li>Quel est mon potentiel de réduction de consommation énergétique</li>
      <li>Quel est la solution technique présentant les coûts minimaux entre investissements et économies</li>
    </ul>
  </section>

  <section class="details body">
    <p>L'amélioration de l'efficacité énergétique est liée directement à l'exploitation des potentiels de récupération du procédé. Des potentiels de diminution de la consommation de 10 à 30% sont usuels. Nous pouvons également améliorer les performances opérationnelles en analysant vos méthodes de fabrication.</p>
    <p>L'analyse Pinch est aussi bien adaptée pour les PME que pour les grandes entreprises dont les procédés sont exploités de manière continue ou discontinue (batch).</p>
    <p>Etant donné les objectifs énergétiques de la confédération, <strong>l'agence nationale de l'énergie (ANE) soutient les analyses Pinch à hauteur de 35% pour les procédés continus et de 60% pour les procédés discontinus (batch).</strong></p>
    <p>Pour tous compléments d'informations et pour savoir si une analyse Pinch est justifiée dans votre cas, nous vous conseillons avec plaisir.</p>
  </section>

  <div class="contact-band"></div>
  <div class="contact">
    <h2>CONTACT//</h2>
    <p>Julien Marchand,<br>Thomas Reynard</p>
  </div>

  <div class="brand">
    <span class="brand-mark"></span>
    <span class="brand-name">THERMALYS</span>
    <span class="brand-sub">PROCESS<br>ENERGY<br>ENGINEERING</span>
  </div>

  <address class="address" style="font-style:normal">
    Thermalys SA<br>Rue des Vergers 14<br>CH-1950 Sion
  </address>
</main>
</body>
</html>
```